Dolan's Auto Business Card
Dolan's Auto Letter Head
Professional
Kevan Dookhoo, MBA, L.L.B.
Managing Director
Corvale Shopping Plaza
14 Tennant Ave
South Valsyan, Trinidad
kevanmail@qorvamail.com
www.dolansauto.com
additional email: kevan@dolansauto.com
LOGO
Drive Open Lead Aim Nurture (D.O.L.A.N)

```html
<!DOCTYPE html>
<html lang="en">
<head>
<meta charset="utf-8">
<title>Dolan's Auto Business Card</title>
<link href="https://fonts.googleapis.com/css2?family=Arimo:wght@400;700&display=swap" rel="stylesheet">
<style>
  :root {
    --stage: #3a3a3a;
    --card-light: #f4f4f4;
    --card-light-edge: #dcdcdc;
    --green-light: #86c84a;
    --green-dark: #3c9a2e;
    --blue: #1f6fc0;
    --blue-light: #6fb3ea;
    --ink-light: #ffffff;
    --brand-red: #d8261c;
  }
  * { margin: 0; padding: 0; box-sizing: border-box; }
  html, body { width: 1200px; height: 574px; overflow: hidden; }
  body {
    background: var(--stage);
    font-family: "Arimo", Arial, sans-serif;
    position: relative;
  }
  .card {
    position: absolute;
    border-radius: 22px;
    overflow: hidden;
    box-shadow: 0 6px 16px rgba(0,0,0,.35);
  }
  .card-front { left: 154px; top: 79px; width: 434px; height: 247px; }
  .card-back {
    left: 619px; top: 250px; width: 430px; height: 252px;
    background: radial-gradient(ellipse at 50% 30%, var(--green-light), var(--green-dark) 85%);
    color: var(--ink-light);
    text-align: center;
  }
  .card-art { position: absolute; inset: 0; width: 100%; height: 100%; }
  .brand {
    position: absolute;
    display: flex; align-items: center; gap: 8px;
    font-weight: 700;
    white-space: nowrap;
  }
  .card-front .brand { left: 14px; top: 106px; color: var(--brand-red); font-size: 22px; }
  .card-back .brand { left: 0; right: 0; top: 72px; justify-content: center; color: var(--ink-light); font-size: 34px; }
  .brand-dot { width: 18px; height: 18px; border-radius: 50%; background: var(--green-dark); flex: none; }
  .card-back .brand-dot { width: 26px; height: 26px; background: var(--blue); }
  .contact {
    position: absolute; right: 12px; top: 10px; width: 190px;
    color: var(--ink-light); text-align: right; font-size: 10px; line-height: 14.5px;
  }
  .contact .name { font-weight: 700; font-size: 10.5px; }
  .contact .address { margin-top: 12px; }
  .contact .lines { margin-top: 26px; }
  .contact .row { display: flex; justify-content: flex-end; align-items: center; gap: 7px; }
  .contact .row svg { width: 8px; height: 8px; flex: none; }
  .contact .gap { height: 7px; }
  .tagline { position: absolute; left: 0; right: 0; top: 122px; font-size: 13px; }
  .web { position: absolute; left: 0; right: 0; top: 222px; font-size: 11px; }
</style>
</head>
<body>
  <section class="card card-front">
    <svg class="card-art" viewBox="0 0 434 247" preserveAspectRatio="none">
      <defs>
        <linearGradient id="front-light" x1="0" y1="0" x2="1" y2="1">
          <stop offset="0" stop-color="#f4f4f4"/>
          <stop offset="1" stop-color="#dcdcdc"/>
        </linearGradient>
        <linearGradient id="front-green" x1="0" y1="0" x2="0" y2="1">
          <stop offset="0" stop-color="#86c84a"/>
          <stop offset="1" stop-color="#3c9a2e"/>
        </linearGradient>
      </defs>
      <rect width="434" height="247" fill="url(#front-light)"/>
      <path d="M200 0 C188 80 220 160 196 247 L218 247 C240 160 208 80 222 0 Z" fill="#6fb3ea"/>
      <path d="M208 0 C196 80 228 160 206 247 L226 247 C246 160 214 80 228 0 Z" fill="#1f6fc0"/>
      <path d="M226 0 C212 80 244 160 224 247 L434 247 L434 0 Z" fill="url(#front-green)"/>
    </svg>
    <div class="brand"><span class="brand-dot"></span>Dolan's Auto</div>
    <div class="contact">
      <div class="name">Kevan Dookhoo, MBA, L.L.B.</div>
      <div>Managing Director</div>
      <div class="address">Corvale Shopping Plaza<br>14 Tennant Ave<br>South Valsyan, Trinidad</div>
      <div class="lines">
        <div class="row">(305) 555-0142 (M)<svg viewBox="0 0 10 10"><path d="M2 0h2l1 3-1.5 1a6 6 0 0 0 2.5 2.5L7 5l3 1v2a2 2 0 0 1-2 2A8 8 0 0 1 0 2a2 2 0 0 1 2-2z" fill="currentColor"/></svg></div>
        <div class="row">(868) 555-0177<svg viewBox="0 0 10 10"><path d="M2 0h2l1 3-1.5 1a6 6 0 0 0 2.5 2.5L7 5l3 1v2a2 2 0 0 1-2 2A8 8 0 0 1 0 2a2 2 0 0 1 2-2z" fill="currentColor"/></svg></div>
        <div class="row">(868) 555-0193<svg viewBox="0 0 10 10"><rect x="2.5" y="0" width="5" height="10" rx="1" fill="currentColor"/></svg></div>
        <div class="row">(954) 555-0128<svg viewBox="0 0 10 10"><rect x="1" y="3" width="8" height="6" fill="currentColor"/><rect x="3" y="0" width="4" height="3" fill="currentColor"/></svg></div>
        <div class="gap"></div>
        <div class="row">kevanmail@qorvamail.com<svg viewBox="0 0 10 10"><rect x="0" y="2" width="10" height="6" fill="currentColor"/></svg></div>
        <div class="row">kevan@dolansauto.com<svg viewBox="0 0 10 10"><rect x="0" y="2" width="10" height="6" fill="currentColor"/></svg></div>
        <div class="row">www.dolansauto.com<svg viewBox="0 0 10 10"><circle cx="5" cy="5" r="4.5" fill="currentColor"/></svg></div>
      </div>
    </div>
  </section>

  <section class="card card-back">
    <div class="brand"><span class="brand-dot"></span>Dolan's Auto</div>
    <p class="tagline">Drive Open Lead Aim Nurture (D.O.L.A.N)</p>
    <p class="web">www.dolansauto.com</p>
  </section>
</body>
</html>
```